Flyer Redesign for Commerical Painting Company in South Australia

RK MARLOW COATINGS — CAPABILITY FLYER SET REFRESH
We are RK Marlow Coatings Contractors, a family-owned painting business in Adelaide, South Australia, trading since 1982. We have five existing capability flyers — Strata, Heritage, Facilities Maintenance, Commercial, and Aged Care. We would like an additional 6th one done that is 'Designer/Architect' aimed. They work, but they look templated. We want them rebuilt as one premium, on-brand family: same look on every page, elevated execution, and zero design inconsistency between them.
IMPORTANT: This is a SET, not five separate jobs. The single most important outcome is that all five look like they were made by the same studio at the same time. Nail one master layout and flow all five flyers through it.
BRAND ASSETS
Our Style Guide plus logos are attached and is the source of truth. The colours, fonts, and logo usage in the guide override anything you see in the current flyers.
Quick orientation:
- Logo: "RK MARLOW COATINGS" stacked mark with the multi-shape icon (red / blue / yellow), sitting above the strapline HERITAGE | COMMERCIAL | RESIDENTIAL. Always keep that strapline locked to the logo.
- Brand colours: blue (primary), red (signal), yellow (accent). Use the exact hex/CMYK values in the Style Guide.
- Tone: established, trusted, award-winning, family-owned.
If any asset (font file, vector logo, hex codes) is missing from the attachment, please ask before starting — do not substitute look-alikes.
WHAT TO KEEP
These elements already create cohesion — keep the concept, just raise the craft:
- The top credentials row of six icons (24-Hour Quote, Professional Project Management, 5-Year Workmanship Warranty, Experience, Guild Finishers Medal, Quality Paints). Keep six markers; redraw the icons in one consistent premium style.
- A large hero image near the top of page 1.
- Three supporting columns of body copy.
- A "Featured Projects" page 2 with a clean image grid and captions.
- A footer band carrying the contact and tagline.
WHAT TO CHANGE
- Replace the light-blue / cyan title banner blocks. They look dated. Use a restrained premium header instead — brand navy, or clean white with a single thin accent rule. No bright cyan fill.
- Change centred body copy to left-aligned text on a strict grid. Left-alignment reads more professional.
- Add whitespace. Give the copy room to breathe. Premium means generous margins, not crammed text.
- Use one bespoke, consistent icon set. Standardise the label wording and length.
- Use one identical footer system across all five flyers.
- Make the hero imagery the visual anchor — larger, sharper, with the same framing treatment applied identically on every flyer.
- Establish a clear premium type hierarchy (display heading, section heading, body, caption) per the Style Guide and apply it identically across all five.
- The only thing that should differ between flyers is a single category accent (e.g. a category label or one tinted element) so each service is instantly readable. Structure, type, footer, and icon row stay identical.
COPY
Please use the copy that is currently in the documents. This may change for us in the future but it will suit for the time being.
For the 'Designer/Architect' flyer please use this copy:
RK Marlow Coatings Contractors is a proud South Australian family-owned business
that has been helping clients transform and maintain their properties for over 40
years.
Founded in 1982, we have built our reputation on quality workmanship, honest
communication, and lasting relationships. Whether it's a family home, apartment
complex, office space, retail environment, heritage building, or commercial interior,
we understand that paint plays an important role in creating spaces that people enjoy
living and working in.
Our team of fully employed, trade-qualified painters takes pride in delivering
exceptional finishes that not only enhance the appearance of a property but also
complement its character, atmosphere, and purpose. From refreshing residential
interiors to revitalising commercial environments and preserving heritage assets, we
work closely with our clients to achieve results that are both practical and visually
appealing.
Our services include:
ï‚· External Painting
ï‚· Internal Painting
ï‚· Wallpaper Installation & Removal
ï‚· French Wash Finishes
ï‚· Lime Wash Application
ï‚· Heritage Restoration, Conservation & Maintenance Works
ï‚· Low VOC & Leaf Mark Approved Coating Applications
ï‚· High Access Painting & Maintenance Works
As a family business, we believe in personal service, attention to detail, and treating
every project as if it were our own. This commitment has earned us the trust of
homeowners, businesses, and property managers across South Australia for more
than four decades.
At RK Marlow Coatings Contractors, we're passionate about creating spaces that look
beautiful, feel welcoming, and stand the test of time while protecting and preserving
the assets entrusted to our care.
FORMAT AND SPECS
- Size: A4 portrait (210 x 297 mm), 2 pages per flyer (front + Featured Projects).
- Bleed: 3 mm all edges, with crop marks on the print export.
- Colour: supply both a print-ready CMYK version (PDF/X) and a digital RGB version (these are emailed and viewed on screen as well as printed).
- Resolution: 300 dpi for all placed imagery.
DELIVERABLES
For each of the 6 flyers (both pages):
1. Print-ready PDF (CMYK, 3 mm bleed, crop marks).
2. Digital PDF (RGB, no bleed/marks, optimised for email).
3. PNG or JPG of each page (RGB, for web/social).
4. We would like an editable file so we can change the copy when required and images. We predominantly use Canva in these situations but are open to suggestion.
PLEASE AVOID
- Bright cyan / baby-blue banner fills. We would be okay using the #01385D colour.
- Centred body paragraphs.
- Stock-photo cliches (handshakes, ladders, generic team shots) — use the project imagery we supply or just have a boxed area where we can add imagery.
- More than three accent colours on a page.
- Drop shadows, bevels, or gradients that fight the clean brand look.
- Any deviation in layout, type, or footer between the five flyers.
HOW WE WILL LOOK AT SUBMISSIONS
1. Cohesion — do all five read as one family? (Most important.)
2. Premium feel — does it look like a high-end contractor, not a template?
3. Brand fidelity — does it match the attached Style Guide?
4. Usability — clean hierarchy, legible, print and screen ready.
RK Marlow Coatings Contractors — Heritage | Commercial | Residential. Trusted across South Australia since 1982.

```html
<!DOCTYPE html>
<html lang="en">
<head>
<meta charset="utf-8">
<title>RK Marlow Coatings – Designer &amp; Architect Services Flyer</title>
<link href="https://fonts.googleapis.com/css2?family=Barlow+Condensed:wght@500;600&family=Barlow+Semi+Condensed:wght@500;600&family=Inter:wght@400;500&display=swap" rel="stylesheet">
<style>
  :root{
    --navy:#14385f;
    --sky:#2a9fd8;
    --yellow:#ffe500;
    --ink:#1d1d1f;
    --stage:#a0a1a5;
    --tile:#efefef;
    --white:#ffffff;
  }
  *{box-sizing:border-box;margin:0;padding:0}
  html,body{width:1200px;height:853px;overflow:hidden;background:var(--stage)}
  body{position:relative;font-family:"Inter",sans-serif;color:var(--ink)}

  .page{position:absolute;top:72px;width:499px;height:706px;background:var(--white);overflow:hidden}
  .page--services{left:71px}
  .page--projects{left:636px}

  /* header */
  .masthead{position:absolute;left:0;top:0;width:100%;height:99px;background:var(--navy)}
  .brand{position:absolute;left:20px;top:22px;width:84px;text-align:center;color:var(--white)}
  .brand__mark{display:block;width:12px;height:12px;background:var(--yellow);margin:0 auto 6px}
  .brand__name{font-family:"Barlow Condensed",sans-serif;font-weight:600;font-size:15px;line-height:14px;letter-spacing:.3px}
  .brand__strap{font-family:"Barlow Condensed",sans-serif;font-weight:500;font-size:3.6px;letter-spacing:.4px;margin-top:5px;white-space:nowrap}
  .masthead__rule{position:absolute;left:123px;top:11px;width:1px;height:71px;background:rgba(255,255,255,.45)}
  .masthead__title{position:absolute;left:154px;top:16px;font-family:"Barlow Semi Condensed",sans-serif;font-weight:600;font-size:29px;line-height:32px;color:var(--white)}
  .masthead__title .accent{color:var(--sky)}

  /* hero */
  .hero{position:absolute;left:0;top:99px;width:100%;height:174px;background:linear-gradient(120deg,#cbb9a2 0%,#e9e5df 35%,#f4f2ef 60%,#d8cfc4 100%)}

  /* credentials */
  .credentials{position:absolute;left:12px;top:288px;width:476px;height:79px;border:1px solid var(--navy);border-radius:0 24px 0 24px;display:flex}
  .cred{position:relative;border-right:1px solid var(--navy);padding:9px 0 0 13px}
  .cred:last-child{border-right:none}
  .cred svg{width:21px;height:21px;stroke:var(--sky);fill:none;stroke-width:1.6;stroke-linecap:round;stroke-linejoin:round}
  .cred__label{position:absolute;left:13px;bottom:10px;font-family:"Barlow Semi Condensed",sans-serif;font-weight:500;font-size:8.6px;line-height:11px;color:var(--ink);text-transform:uppercase}

  /* columns */
  .col{position:absolute;top:382px;width:142px}
  .col--about{left:15px}
  .col--team{left:179px}
  .col--services{left:344px;width:146px}
  .tab{display:inline-block;background:var(--yellow);color:var(--navy);font-family:"Barlow Semi Condensed",sans-serif;font-weight:600;font-size:12px;line-height:19px;padding:0 8px 0 6px;border-radius:0 7px 0 0;margin-bottom:6px}
  .body{font-size:7.9px;line-height:10.1px;text-align:justify;color:var(--ink)}
  .body + .body{margin-top:7px}
  .services{list-style:none}
  .services li{position:relative;padding-left:11px;font-size:7.9px;line-height:9px;margin-bottom:8px}
  .services li::before{content:"";position:absolute;left:2px;top:2px;border-left:3px solid var(--sky);border-top:2.5px solid transparent;border-bottom:2.5px solid transparent}

  .closing{position:absolute;top:584px;font-size:7.9px;line-height:10.1px;text-align:justify}
  .closing--left{left:14px;width:220px}
  .closing--right{left:272px;width:208px}
  .closing__rule{position:absolute;left:252px;top:580px;width:1px;height:52px;background:var(--navy)}

  /* footer */
  .footer{position:absolute;left:0;top:647px;width:100%;height:59px;background:var(--navy);border-radius:0 40px 0 0;color:var(--white)}
  .footer__bar{position:absolute;top:13px;width:2px;height:27px;background:var(--yellow)}
  .footer__tagline{position:absolute;left:27px;top:11px;font-family:"Barlow Condensed",sans-serif;font-weight:500;font-size:13px;line-height:15px}
  .footer__contact{position:absolute;left:414px;top:11px;font-family:"Barlow Condensed",sans-serif;font-weight:500;font-size:13px;line-height:15px}
  .footer__phone{color:var(--yellow);font-weight:600}

  /* projects */
  .project{position:absolute;width:231px}
  .project__photo{width:231px;height:131px;background:var(--tile);border-radius:22px 0 22px 0}
  .project__caption{position:relative;margin-top:9px;padding-left:13px;height:26px}
  .project__caption::before{content:"";position:absolute;left:0;top:0;width:2px;height:26px;background:var(--yellow)}
  .project__site{font-family:"Barlow Semi Condensed",sans-serif;font-weight:600;font-size:10px;line-height:13px;color:var(--navy)}
  .project__scope{font-size:9.6px;line-height:13px;color:var(--navy)}
</style>
</head>
<body>

<!-- Page 1 -->
<section class="page page--services">
  <header class="masthead">
    <div class="brand">
      <span class="brand__mark"></span>
      <div class="brand__name">RK MARLOW<br>COATINGS</div>
      <div class="brand__strap">HERITAGE | COMMERCIAL | RESIDENTIAL</div>
    </div>
    <div class="masthead__rule"></div>
    <h1 class="masthead__title"><span class="accent">DESIGNER &amp; ARCHITECT</span><br>SERVICES</h1>
  </header>

  <div class="hero" role="img" aria-label="Designer sketching an interior plan beside fabric, timber and tile samples"></div>

  <div class="credentials">
    <div class="cred" style="width:75px">
      <svg viewBox="0 0 24 24"><rect x="4" y="3" width="15" height="18" rx="2"/><path d="M8 8h7M8 12h7M8 16h4"/></svg>
      <div class="cred__label">24-hour<br>quote turn-<br>around</div>
    </div>
    <div class="cred" style="width:78px">
      <svg viewBox="0 0 24 24"><circle cx="9" cy="6" r="3.5"/><path d="M2 20v-3a5 5 0 0 1 8-4"/><circle cx="17" cy="16" r="3"/><path d="M17 11v1.5M17 19.5V21M12 16h1.5M20.5 16H22"/></svg>
      <div class="cred__label">professional<br>project<br>management</div>
    </div>
    <div class="cred" style="width:79px">
      <svg viewBox="0 0 24 24"><path d="M12 3l7 3v6c0 4-3 7-7 9-4-2-7-5-7-9V6z"/><path d="M9 12l2 2 4-4"/></svg>
      <div class="cred__label">5-year<br>workmanship<br>warranty</div>
    </div>
    <div class="cred" style="width:73px">
      <svg viewBox="0 0 24 24"><rect x="4" y="3" width="14" height="5" rx="1"/><path d="M18 5h2v5h-8v3"/><rect x="10.5" y="13" width="3" height="8" rx="1"/></svg>
      <div class="cred__label">43-years<br>painting<br>experience</div>
    </div>
    <div class="cred" style="width:84px">
      <svg viewBox="0 0 24 24"><path d="M7 3h10v6a5 5 0 0 1-10 0z"/><path d="M7 5H4v2a3 3 0 0 0 3 3M17 5h3v2a3 3 0 0 1-3 3M12 14v4M8 21h8"/></svg>
      <div class="cred__label">guild<br>finishers medal<br>2024</div>
    </div>
    <div class="cred" style="flex:1">
      <svg viewBox="0 0 24 24"><path d="M6 4h12l4 5-10 12L2 9z"/><path d="M2 9h20M9 4l3 17M15 4l-3 17"/></svg>
      <div class="cred__label">only the<br>highest quality<br>paints</div>
    </div>
  </div>

  <div class="col col--about">
    <h2 class="tab">ABOUT RK MARLOW</h2>
    <p class="body">RK Marlow Coatings Contractors is a proud South Australian family-owned business that has been helping clients transform and maintain their properties for over 40 years.</p>
    <p class="body">Founded in 1982, we have built our reputation on quality workmanship, honest communication, and lasting relationships. Whether it's a family home, apartment complex, office space, retail environment, heritage building, or commercial interior, we understand that paint plays an important role in creating spaces that people enjoy living and working in.</p>
  </div>

  <div class="col col--team">
    <h2 class="tab">OUR TEAM</h2>
    <p class="body">Our team of fully employed, trade-qualified painters takes pride in delivering exceptional finishes that not only enhance the appearance of a property but also complement its character, atmosphere, and purpose.</p>
    <p class="body">From refreshing residential interiors to revitalising commercial environments and preserving heritage assets, we work closely with our clients to achieve results that are both practical and visually appealing.</p>
  </div>

  <div class="col col--services">
    <h2 class="tab">OUR SERVICES</h2>
    <ul class="services">
      <li>External Painting</li>
      <li>Internal Painting</li>
      <li>Wallpaper Installation &amp; Removal</li>
      <li>French Wash Finishes</li>
      <li>Lime Wash Application</li>
      <li>Heritage Restoration, Conservation &amp; Maintenance Works</li>
      <li>Low VOC &amp; Leaf Mark Approved Coatings</li>
      <li>High Access Painting &amp; Maintenance Works</li>
    </ul>
  </div>

  <p class="closing closing--left">As a family business, we believe in personal service, attention to detail, and treating every project as if it were our own. This commitment has earned us the trust of homeowners, businesses, and property managers across South Australia for more than four decades.</p>
  <div class="closing__rule"></div>
  <p class="closing closing--right">At RK Marlow Coatings Contractors, we're passionate about creating spaces that look beautiful, feel welcoming, and stand the test of time while protecting and preserving the assets entrusted to our care.</p>

  <footer class="footer">
    <span class="footer__bar" style="left:15px"></span>
    <p class="footer__tagline">Every commercial project is important to us, and we<br>apply our expertise to each one.</p>
    <span class="footer__bar" style="left:402px"></span>
    <p class="footer__contact">DANA RENSHAW<br><span class="footer__phone">0412 730 258</span></p>
  </footer>
</section>

<!-- Page 2 -->
<section class="page page--projects">
  <header class="masthead">
    <div class="brand">
      <span class="brand__mark"></span>
      <div class="brand__name">RK MARLOW<br>COATINGS</div>
      <div class="brand__strap">HERITAGE | COMMERCIAL | RESIDENTIAL</div>
    </div>
    <div class="masthead__rule"></div>
    <h1 class="masthead__title" style="top:18px;font-size:30px">FEATURED<br><span class="accent">PROJECTS</span></h1>
  </header>

  <article class="project" style="left:13px;top:113px"><div class="project__photo" role="img" aria-label="Project photo"></div><div class="project__caption"><p class="project__site">SEACLIFF RISE | HARBANE BUILT</p><p class="project__scope">Full External Repaint</p></div></article>
  <article class="project" style="left:255px;top:113px"><div class="project__photo" role="img" aria-label="Project photo"></div><div class="project__caption"><p class="project__site">SEACLIFF RISE | HARBANE BUILT</p><p class="project__scope">Full External Repaint</p></div></article>
  <article class="project" style="left:13px;top:293px"><div class="project__photo" role="img" aria-label="Project photo"></div><div class="project__caption"><p class="project__site">SEACLIFF RISE | HARBANE BUILT</p><p class="project__scope">Full External Repaint</p></div></article>
  <article class="project" style="left:255px;top:293px"><div class="project__photo" role="img" aria-label="Project photo"></div><div class="project__caption"><p class="project__site">SEACLIFF RISE | HARBANE BUILT</p><p class="project__scope">Full External Repaint</p></div></article>
  <article class="project" style="left:13px;top:469px"><div class="project__photo" role="img" aria-label="Project photo"></div><div class="project__caption"><p class="project__site">SEACLIFF RISE | HARBANE BUILT</p><p class="project__scope">Full External Repaint</p></div></article>
  <article class="project" style="left:255px;top:469px"><div class="project__photo" role="img" aria-label="Project photo"></div><div class="project__caption"><p class="project__site">SEACLIFF RISE | HARBANE BUILT</p><p class="project__scope">Full External Repaint</p></div></article>

  <footer class="footer">
    <span class="footer__bar" style="left:15px"></span>
    <p class="footer__tagline">Every commercial project is important to us, and we<br>apply our expertise to each one.</p>
    <span class="footer__bar" style="left:402px"></span>
    <p class="footer__contact">DANA RENSHAW<br><span class="footer__phone">0412 730 258</span></p>
  </footer>
</section>

</body>
</html>
```